Need Business Cards for my Business

email address: rkpmarlowhollowworks@vendrimail.com
web address: rkpmarlowhollowworks.net
Slogan: We offer various QVN licenses
Rowland K. Pemberly
Please stick with colors of Company Logo
would like the card to be more of the color example of the logo.
If you need PDF copy of logo email me at the above account.
Creative control rests with you.

Industry/Entity Type

Business

Contact Information for Business Card

I am a minimalist, but would like something to pop and stand out amongst other cards, make it memorable.

Font styles to use
Serif
Decorative
Script

```html
<!DOCTYPE html>
<html lang="en">
<head>
<meta charset="utf-8">
<title>RKP Marlow Hollow Works – Business Card</title>
<link rel="stylesheet" href="https://fonts.googleapis.com/css2?family=Oswald:wght@500&family=Open+Sans:wght@400;600;700&display=swap">
<style>
  :root {
    --red: #d8212b;
    --red-deep: #b5121c;
    --blue: #1f7cc4;
    --white: #ffffff;
    --paper: #f6f6f6;
    --stage: #e4e5e7;
  }
  html, body {
    margin: 0;
    width: 1200px;
    height: 900px;
    overflow: hidden;
    background: var(--stage);
  }
  .stage {
    position: relative;
    width: 1200px;
    height: 900px;
  }
  .card {
    position: absolute;
    top: 152px;
    width: 340px;
    height: 595px;
    overflow: hidden;
    background: var(--red);
    box-shadow: 0 14px 30px rgba(0,0,0,.22);
  }
  .card-front { left: 200px; }
  .card-back  { left: 660px; }
  .card svg.shapes {
    position: absolute;
    inset: 0;
  }
  .front-name {
    position: absolute;
    left: 28px;
    top: 150px;
    width: 290px;
    font-family: "Open Sans", sans-serif;
    font-weight: 700;
    color: var(--white);
    font-size: 30px;
    line-height: 1.05;
    letter-spacing: 1px;
    text-transform: uppercase;
  }
  .back-brand {
    position: absolute;
    top: 62px;
    left: 0;
    right: 0;
    display: flex;
    align-items: center;
    justify-content: center;
    gap: 12px;
  }
  .back-brand .dot {
    width: 18px;
    height: 18px;
    border-radius: 50%;
    background: var(--red);
  }
  .back-brand .name {
    font-family: "Open Sans", sans-serif;
    font-weight: 700;
    font-size: 19px;
    color: var(--blue);
    letter-spacing: 1px;
    text-transform: uppercase;
    line-height: 1.1;
  }
  .details {
    position: absolute;
    top: 232px;
    left: 0;
    right: 0;
    text-align: center;
    color: var(--white);
    font-family: "Open Sans", sans-serif;
  }
  .person {
    font-family: "Oswald", sans-serif;
    font-weight: 500;
    font-size: 30px;
    letter-spacing: .5px;
    text-transform: uppercase;
    line-height: 1;
  }
  .role {
    font-size: 15px;
    letter-spacing: 1px;
    text-transform: uppercase;
    margin-top: 4px;
  }
  .icon {
    display: block;
    margin: 16px auto 6px;
    width: 24px;
    height: 24px;
  }
  .contact {
    font-size: 11.5px;
  }
  .divider {
    display: flex;
    align-items: center;
    gap: 10px;
    margin: 18px 26px 6px;
  }
  .divider .rule {
    flex: 1;
    height: 1px;
    background: var(--white);
  }
  .divider .icon { margin: 0; }
  .company {
    font-weight: 700;
    font-size: 13px;
    letter-spacing: .5px;
    text-transform: uppercase;
    margin-top: 8px;
  }
  .address {
    font-size: 11.5px;
    line-height: 1.45;
    margin-top: 2px;
  }
</style>
</head>
<body>
<main class="stage">

  <section class="card card-front" aria-label="Card front">
    <svg class="shapes" viewBox="0 0 340 595" width="340" height="595">
      <defs>
        <linearGradient id="frontRed" x1="0" y1="0" x2="1" y2="1">
          <stop offset="0" stop-color="#e2262f"/>
          <stop offset="1" stop-color="#c3161f"/>
        </linearGradient>
      </defs>
      <rect width="340" height="595" fill="url(#frontRed)"/>
      <path d="M0,128 C30,360 170,450 340,462 L340,595 L118,595 C80,548 34,508 0,488 Z" fill="var(--white)"/>
      <path d="M0,128 C30,360 170,450 340,462" fill="none" stroke="var(--blue)" stroke-width="11"/>
    </svg>
    <div class="front-name">RKP Marlow<br>Hollow Works</div>
  </section>

  <section class="card card-back" aria-label="Card back">
    <svg class="shapes" viewBox="0 0 340 595" width="340" height="595">
      <defs>
        <linearGradient id="backRed" x1="0" y1="0" x2="1" y2="1">
          <stop offset="0" stop-color="#e0303a"/>
          <stop offset="1" stop-color="#b5121c"/>
        </linearGradient>
      </defs>
      <rect width="340" height="595" fill="url(#backRed)"/>
      <path d="M0,0 H340 V150 C250,186 110,186 0,160 Z" fill="var(--white)"/>
      <path d="M0,160 C110,186 250,186 340,150" fill="none" stroke="var(--blue)" stroke-width="8"/>
    </svg>

    <div class="back-brand">
      <span class="dot"></span>
      <span class="name">RKP Marlow<br>Hollow Works</span>
    </div>

    <div class="details">
      <div class="person">Rowland K. Pemberly</div>
      <div class="role">General Manager</div>

      <svg class="icon" viewBox="0 0 24 24" aria-hidden="true">
        <circle cx="12" cy="12" r="11" fill="none" stroke="#fff" stroke-width="1.4"/>
        <rect x="6.5" y="8.5" width="11" height="7.5" fill="none" stroke="#fff" stroke-width="1.3"/>
        <path d="M6.5,8.5 L12,13 L17.5,8.5" fill="none" stroke="#fff" stroke-width="1.3"/>
      </svg>
      <div class="contact">rkpmarlowhollowworks@vendrimail.com</div>

      <svg class="icon" viewBox="0 0 24 24" aria-hidden="true">
        <circle cx="12" cy="12" r="11" fill="none" stroke="#fff" stroke-width="1.4"/>
        <circle cx="12" cy="12" r="6" fill="none" stroke="#fff" stroke-width="1.3"/>
        <path d="M6,12 H18 M12,6 C9,9 9,15 12,18 M12,6 C15,9 15,15 12,18" fill="none" stroke="#fff" stroke-width="1.1"/>
      </svg>
      <div class="contact">rkpmarlowhollowworks.net</div>

      <div class="divider">
        <span class="rule"></span>
        <svg class="icon" viewBox="0 0 24 24" aria-hidden="true">
          <circle cx="12" cy="12" r="11" fill="none" stroke="#fff" stroke-width="1.4"/>
          <path d="M12,18 C9,14 8,12 8,10 A4,4 0 0 1 16,10 C16,12 15,14 12,18 Z" fill="none" stroke="#fff" stroke-width="1.3"/>
          <circle cx="12" cy="10" r="1.4" fill="#fff"/>
        </svg>
        <span class="rule"></span>
      </div>

      <div class="company">RKP Marlow Hollow Works</div>
      <div class="address">West 18th Lane, 9th Floor, Harlow City, HC 204<br>Avalonia</div>
    </div>
  </section>

</main>
</body>
</html>
```